Brennock Metal recycling, a business card/logo for our industrial family metal recycling company

A new business card design/logo for our long established family metal recycling company.
I have a logo for our property company which was designed a few months ago on pixel forum which I would like to be very close to this design but have a more industrial feel to it and in a darker blue colour, please see attachments.

Target Market(s)

industries that produce metal waste for recycling, construction sites, engineering companies, manufactures, builders, plumbers, electricians, general house holders.

Industry/Entity Type

Recycling

Contact Information for Business Card

owner/director...Gordon brennock
e-mail....info@brennockscrapworks.example.co.uk
web address.....brennockscrapworks.example.co.uk

Font styles to use
Serif
Sans Serif

Colors
0255a3
ffffff

Requirements
Must have
• -dark blue business card on front.
-white on the back, see contact details, e-mail address for metal company.
-to have an industrial feel to it.
-brennock logo as business card attached but (brennock metal recycling)
please remove the little roof/arrow above brennock as this was relevant to property company.
Nice to have
• please see our website brennockscrapworks.example.co.uk with all details
being correct however I would like to refresh the logo to more like the brennock property investment business card logo attached.
Should not have
• should not contain details from property investments card as this design is for the metal recycling company.

```html
<!DOCTYPE html>
<html lang="en">
<head>
<meta charset="utf-8">
<title>Brennock Metal Recycling – Business Card</title>
<link href="https://fonts.googleapis.com/css2?family=Montserrat:wght@500;700;800&family=Roboto:wght@400&display=swap" rel="stylesheet">
<style>
  :root {
    --navy: #0b2450;
    --navy-deep: #061a3c;
    --red: #b21e2b;
    --white: #ffffff;
    --ink: #13294f;
    --stage: #d6d5d2;
  }
  * { box-sizing: border-box; margin: 0; padding: 0; }
  html, body {
    width: 1200px; height: 801px; overflow: hidden;
    background: var(--stage);
  }
  .canvas {
    position: relative; width: 1200px; height: 801px;
    display: flex; align-items: center; justify-content: center; gap: 40px;
  }
  .card {
    position: relative; width: 540px; height: 309px; overflow: hidden;
    box-shadow: 0 6px 18px rgba(0,0,0,.18);
  }

  /* Contact side */
  .card--contact { background: var(--white); }
  .brand {
    position: absolute; display: flex; align-items: center; gap: 12px;
    font-family: "Montserrat", sans-serif; font-weight: 800;
    color: var(--ink); text-transform: uppercase; line-height: 1;
  }
  .brand__dot { border-radius: 50%; background: var(--red); flex: none; }
  .card--contact .brand { left: 34px; top: 44px; font-size: 27px; letter-spacing: .5px; }
  .card--contact .brand__dot { width: 34px; height: 34px; }

  .person {
    position: absolute; left: 34px; top: 138px; width: 200px;
    font-family: "Montserrat", sans-serif; text-align: right;
  }
  .person__name { font-weight: 700; font-size: 19px; color: var(--ink); text-transform: uppercase; }
  .person__role { font-weight: 500; font-size: 15px; color: var(--red); margin-top: 3px; }

  .divider { position: absolute; left: 250px; top: 132px; width: 1.5px; height: 62px; background: var(--ink); }

  .contacts {
    position: absolute; left: 264px; top: 132px; list-style: none;
    font-family: "Roboto", sans-serif; font-size: 12.5px; color: var(--ink);
  }
  .contacts li { display: flex; align-items: center; gap: 6px; height: 21px; white-space: nowrap; }
  .contacts svg { width: 12px; height: 12px; fill: var(--red); flex: none; }

  .address-band {
    position: absolute; left: 0; bottom: 22px; width: 100%; height: 38px; display: flex;
  }
  .address-band__main {
    flex: 1; background: var(--navy-deep); color: var(--white);
    font-family: "Roboto", sans-serif; font-size: 14px;
    display: flex; align-items: center; padding-left: 34px;
  }
  .address-band__accent { width: 90px; background: var(--red); }

  /* Brand side */
  .card--brand {
    background: linear-gradient(160deg, var(--navy) 0%, var(--navy-deep) 100%);
    display: flex; align-items: center; justify-content: center;
  }
  .card--brand .brand { position: static; color: var(--white); font-size: 30px; }
  .card--brand .brand__dot { width: 40px; height: 40px; }
</style>
</head>
<body>
<main class="canvas">

  <section class="card card--contact" aria-label="Business card, contact side">
    <div class="brand"><span class="brand__dot"></span>Brennock Metal Recycling</div>

    <div class="person">
      <p class="person__name">Gordon Brennock</p>
      <p class="person__role">Director</p>
    </div>
    <div class="divider"></div>

    <ul class="contacts">
      <li>
        <svg viewBox="0 0 24 24" aria-hidden="true"><path d="M6.6 10.8a15 15 0 0 0 6.6 6.6l2.2-2.2a1 1 0 0 1 1-.25 11.4 11.4 0 0 0 3.6.57 1 1 0 0 1 1 1V20a1 1 0 0 1-1 1A17 17 0 0 1 3 4a1 1 0 0 1 1-1h3.5a1 1 0 0 1 1 1c0 1.25.2 2.45.57 3.6a1 1 0 0 1-.25 1z"/></svg>
        020 - 7946 - 0321
      </li>
      <li>
        <svg viewBox="0 0 24 24" aria-hidden="true"><path d="M2 5h20v14H2zm2 2v.5l8 5 8-5V7zm0 2.8V17h16V9.8l-8 5z"/></svg>
        info@brennockscrapworks.example.co.uk
      </li>
      <li>
        <svg viewBox="0 0 24 24" aria-hidden="true"><path d="M12 2a10 10 0 1 0 0 20 10 10 0 0 0 0-20zm6.9 6h-3a15 15 0 0 0-1.3-3.9A8 8 0 0 1 18.9 8zM12 4c.8 1.2 1.5 2.5 1.9 4h-3.8c.4-1.5 1.1-2.8 1.9-4zM4.3 14a8 8 0 0 1 0-4h3.4a16 16 0 0 0 0 4zm.8 2h3a15 15 0 0 0 1.3 3.9A8 8 0 0 1 5.1 16zm3-8h-3a8 8 0 0 1 4.3-3.9A15 15 0 0 0 8.1 8zM12 20c-.8-1.2-1.5-2.5-1.9-4h3.8c-.4 1.5-1.1 2.8-1.9 4zm2.3-6H9.7a14 14 0 0 1 0-4h4.6a14 14 0 0 1 0 4zm.3 5.9a15 15 0 0 0 1.3-3.9h3a8 8 0 0 1-4.3 3.9zm1.7-5.9a16 16 0 0 0 0-4h3.4a8 8 0 0 1 0 4z"/></svg>
        brennockscrapworks.example.co.uk
      </li>
    </ul>

    <div class="address-band">
      <p class="address-band__main">Unit 9, 14 Halden Lane, London, SE99 4QZ</p>
      <span class="address-band__accent"></span>
    </div>
  </section>

  <section class="card card--brand" aria-label="Business card, brand side">
    <div class="brand"><span class="brand__dot"></span>Brennock Metal Recycling</div>
  </section>

</main>
</body>
</html>
```